KRL Going Cashless

Hello,
We are a medical office looking to get a flyer created to promote to our patients we will be going "Cashless." Our tagline will be "Cash-Less is Stress-Less"

"Starting in July, to offer you the fastest and most convenient service, we are transitioning to a cashless system. You can now enjoy faster checkout times and greater security with card and contactless payments. More info to come."

I've added two other flyers as sample designs we've used.

Please include logo, addresses, website, phone number

Files to include jpeg, png, pdf (under 5mb), Facebook and Instagram sizing.

Thank you,
Doran

```html
<!DOCTYPE html>
<html lang="en">
<head>
<meta charset="utf-8">
<title>KRL Foot &amp; Ankle – Cashless is Stressless</title>
<link rel="stylesheet" href="https://fonts.googleapis.com/css2?family=Bebas+Neue&family=Great+Vibes&family=Montserrat:ital,wght@0,400;0,500;0,600;0,700;0,800;1,700&display=swap">
<style>
  :root {
    --ink: #333333;
    --paper: #ececec;
    --orange: #ee7b45;
    --teal: #4fc1a6;
    --white: #ffffff;
    --chip: #f6f6f6;
  }
  * { margin: 0; padding: 0; box-sizing: border-box; }
  html, body { width: 927px; height: 1200px; overflow: hidden; background: var(--paper); }
  .flyer {
    position: relative;
    width: 927px;
    height: 1200px;
    overflow: hidden;
    background: linear-gradient(160deg, #f3f3f3 0%, var(--paper) 60%);
    font-family: "Montserrat", sans-serif;
  }
  .dark-field { position: absolute; left: 0; top: 0; width: 927px; height: 1200px; }
  .bottom-band { position: absolute; left: 0; bottom: 0; width: 927px; height: 26px; background: var(--orange); }

  .brand { position: absolute; top: 86px; left: 0; width: 927px; display: flex; justify-content: center; align-items: center; gap: 14px; }
  .brand-mark { width: 30px; height: 30px; background: var(--teal); }
  .brand-name { font-weight: 800; font-size: 32px; color: var(--orange); letter-spacing: 0.5px; }

  .headline {
    position: absolute; left: 150px; top: 196px;
    font-family: "Bebas Neue", sans-serif; font-size: 206px; line-height: 1;
    color: var(--ink); letter-spacing: 1px;
    transform: scaleY(1.08); transform-origin: top left;
  }
  .is { position: absolute; left: 158px; top: 366px; font-weight: 500; font-size: 88px; line-height: 1; color: var(--teal); }
  .script { position: absolute; left: 254px; top: 318px; font-family: "Great Vibes", cursive; font-size: 164px; line-height: 1.1; color: var(--orange); }

  .payment-photo {
    position: absolute; left: 380px; top: 520px; width: 520px; height: 300px;
    border-radius: 60px 40px 70px 40px;
    transform: rotate(28deg);
    transform-origin: center;
    background: linear-gradient(120deg, #8ccdf0 0%, #6a6e72 45%, #3b3d40 100%);
  }

  .starting { position: absolute; left: 88px; top: 566px; font-family: "Bebas Neue", sans-serif; font-size: 70px; line-height: 1; color: var(--white); letter-spacing: 1px; }
  .month { position: absolute; left: 88px; top: 630px; font-family: "Bebas Neue", sans-serif; font-size: 156px; line-height: 1; color: var(--teal); letter-spacing: 4px; }
  .message { position: absolute; left: 88px; top: 774px; width: 335px; font-size: 17.2px; line-height: 21.2px; color: var(--white); }
  .more-info { position: absolute; left: 88px; top: 911px; font-size: 16.5px; font-weight: 700; font-style: italic; color: var(--teal); }
  .phone { position: absolute; left: 88px; top: 966px; font-size: 42px; font-weight: 800; color: var(--orange); letter-spacing: 0.5px; }
  .website { position: absolute; left: 91px; top: 1019px; font-size: 26.5px; font-weight: 700; color: var(--white); }

  .payment-list { position: absolute; left: 85px; top: 1106px; display: flex; gap: 7px; list-style: none; }
  .payment-list li { width: 54px; height: 32px; background: var(--chip); border-radius: 3px; display: flex; align-items: center; justify-content: center; font-size: 8.5px; font-weight: 700; color: var(--ink); }

  .benefit { position: absolute; height: 52px; width: 304px; border-radius: 6px; display: flex; align-items: center; justify-content: center; font-family: "Bebas Neue", sans-serif; font-size: 36px; letter-spacing: 1px; box-shadow: 6px 6px 10px rgba(0,0,0,0.28); }
  .benefit--fast { left: 545px; top: 918px; background: var(--orange); color: var(--white); }
  .benefit--secure { left: 490px; top: 990px; background: var(--paper); color: var(--orange); }
  .benefit--carry { left: 554px; top: 1062px; background: var(--teal); color: var(--white); }
</style>
</head>
<body>
<main class="flyer">
  <svg class="dark-field" viewBox="0 0 927 1200" aria-hidden="true">
    <path d="M0 530 C 200 478, 520 468, 700 560 C 820 690, 790 1000, 768 1176 L 0 1176 Z" fill="#333333"/>
  </svg>

  <header class="brand">
    <span class="brand-mark"></span>
    <span class="brand-name">KRL FOOT &amp; ANKLE</span>
  </header>

  <h1 class="headline">CASHLESS</h1>
  <span class="is">is</span>
  <span class="script">Stressless</span>

  <div class="payment-photo" role="img" aria-label="Hand holding a blue credit card over a grey card payment terminal"></div>

  <p class="starting">STARTING</p>
  <p class="month">IN JULY</p>
  <p class="message">to offer you the fastest and most convenient service, we are transitioning to a cashless system. You can now enjoy faster checkout times and greater security with card and contactless payments.</p>
  <p class="more-info">More info to come.</p>
  <p class="phone">(877) 555-0142</p>
  <p class="website">www.krlfootcare.com</p>

  <ul class="payment-list" aria-label="Accepted payment methods">
    <li>Ardenta</li>
    <li>Tapwell</li>
    <li>Novira</li>
    <li>Wavlo</li>
    <li>Pinecrest</li>
    <li>Lumora</li>
    <li>Quellix</li>
  </ul>

  <div class="benefit benefit--fast">1. Fast Payments</div>
  <div class="benefit benefit--secure">2. Secure Method</div>
  <div class="benefit benefit--carry">3. Easy to Carry</div>

  <div class="bottom-band"></div>
</main>
</body>
</html>
```